5 x 7 card advertising ash spreading

I need a new design for a double sided 5 x 7 horizontal post card to give to funeral homes so they can give them out to people who are interested in an ash spreading boat charter at sea for their loved one who has died. I want a simple, professional, classy, thoughtful design that I can include a summary of what we offer, what's included, our logo and and contact info. Even though we will include the "what" we offer, this piece needs to speak to the readers "why". I've included an AI excerpt about why people desire this as opposed to being buried.
What we offer: Attended service, Unattended service, Memorial service, Anniversary service. What's included: Certificate of Ash Spreading, Onboard refreshments, Personalized music. Our contact information: Tidewell Cruises, www.tidewellcruises.com, 412 Marlow Ave., Clearwater, FL 33761, (727) 584-9130

Target Market(s)

People visiting a funeral home planning their own or a relatives final wishes for ash spreading at sea

Industry/Entity Type

Private boat charters

Requirements
Must have
• Professional look, speaks to they "why", as well as includes the "what" we do.

```html
<!DOCTYPE html>
<html lang="en">
<head>
<meta charset="utf-8">
<title>Tidewell Cruises – Ash Spreading Postcard</title>
<link href="https://fonts.googleapis.com/css2?family=Oswald:wght@400;500;700&display=swap" rel="stylesheet">
<style>
  :root {
    --backdrop: #cdcdcd;
    --navy: #10104a;
    --panel: #f3f3f6;
    --water-deep: #24493f;
    --water-mid: #3a6a5a;
    --water-light: #4f7f6c;
    --white: #ffffff;
  }
  html, body {
    margin: 0;
    padding: 0;
    width: 948px;
    height: 1200px;
    overflow: hidden;
    background: var(--backdrop);
    font-family: "Oswald", sans-serif;
  }
  .sheet { position: relative; width: 948px; height: 1200px; }
  .postcard {
    position: absolute;
    left: 117px;
    width: 714px;
    height: 490px;
    overflow: hidden;
    background: var(--panel);
    box-shadow: 0 0 0 1px rgba(0,0,0,0.08);
  }
  .postcard--front { top: 82px; }
  .postcard--back { top: 628px; }

  .postcard__photo {
    position: absolute;
    inset: 0 0 80px 0;
    background:
      radial-gradient(ellipse at 80% 75%, rgba(235,200,210,0.35), transparent 45%),
      radial-gradient(ellipse at 15% 35%, rgba(230,170,190,0.25), transparent 40%),
      linear-gradient(160deg, var(--water-light) 0%, var(--water-mid) 45%, var(--water-deep) 100%);
  }
  .postcard__panel {
    position: absolute;
    left: 0; top: 0;
    width: 714px; height: 490px;
  }

  .brand {
    position: absolute;
    left: 30px; top: 62px;
    width: 130px;
    display: flex;
    align-items: center;
    gap: 8px;
  }
  .brand__dot {
    flex: 0 0 14px;
    width: 14px; height: 14px;
    border-radius: 50%;
    background: var(--white);
  }
  .brand__name {
    color: var(--white);
    font-weight: 700;
    font-size: 24px;
    line-height: 26px;
    text-transform: uppercase;
    letter-spacing: 0.5px;
  }

  .headline {
    position: absolute;
    left: 193px; top: 38px;
    margin: 0;
    color: var(--white);
    font-weight: 700;
    font-size: 56px;
    line-height: 54px;
    text-transform: uppercase;
    letter-spacing: -2px;
    text-shadow: 0 1px 6px rgba(0,0,0,0.35);
  }

  .info { color: var(--navy); text-transform: uppercase; }
  .info__heading {
    position: absolute;
    margin: 0;
    font-weight: 700;
    font-size: 17px;
    line-height: 1;
    letter-spacing: -0.2px;
  }
  .info__list {
    position: absolute;
    margin: 0; padding: 0;
    list-style: none;
    font-weight: 400;
    letter-spacing: -0.2px;
  }
  .info__list li::before {
    content: "";
    display: inline-block;
    width: 4px; height: 4px;
    border-radius: 50%;
    background: var(--navy);
    margin-right: 6px;
    vertical-align: middle;
  }
  .offer__heading { left: 35px; top: 386px; }
  .offer__list { left: 35px; top: 406px; font-size: 12px; line-height: 16.3px; }
  .included__heading { left: 171px; top: 386px; }
  .included__list { left: 171px; top: 406px; font-size: 11.5px; line-height: 15.2px; }
  .contact__heading { left: 329px; top: 386px; }
  .contact__name {
    position: absolute; left: 329px; top: 405px;
    margin: 0; font-weight: 400; font-size: 18px; line-height: 1;
  }
  .contact__address {
    position: absolute; left: 329px; top: 430px;
    margin: 0; font-weight: 400; font-size: 11px; line-height: 1; letter-spacing: -0.2px;
  }
  .contact__web {
    position: absolute; left: 547px; top: 387px;
    margin: 0; font-weight: 700; font-size: 14px; line-height: 1;
    text-transform: none; letter-spacing: -0.2px;
  }
  .contact__phone {
    position: absolute; left: 547px; top: 406px;
    margin: 0; font-weight: 500; font-size: 24px; line-height: 1; letter-spacing: -0.3px;
  }
  .divider {
    position: absolute;
    top: 386px; height: 64px;
    border-left: 1px dotted var(--navy);
  }
  .divider--a { left: 154px; }
  .divider--b { left: 316px; }
  .divider--c { left: 531px; }
  .rule {
    position: absolute;
    left: 155px; top: 464px;
    width: 532px;
    border-top: 1px solid var(--navy);
  }
  .rule::before {
    content: "";
    position: absolute;
    left: -3px; top: -3.5px;
    width: 6px; height: 6px;
    border-radius: 50%;
    background: var(--navy);
  }
</style>
</head>
<body>
<main class="sheet">

  <article class="postcard postcard--front">
    <div class="postcard__photo" role="img" aria-label="Hand pouring ashes from an urn into green sea water scattered with floating flower petals"></div>
    <svg class="postcard__panel" viewBox="0 0 714 490" aria-hidden="true">
      <polygon points="0,361 143,294 714,377 714,490 0,490" fill="var(--panel)"/>
      <polyline points="0,361 143,294 714,377" fill="none" stroke="var(--navy)" stroke-width="4"/>
    </svg>
    <div class="brand"><span class="brand__dot"></span><span class="brand__name">Tidewell<br>Cruises</span></div>
    <h1 class="headline">Honoring<br>Memories<br>Across the<br>Waves</h1>
    <section class="info">
      <h2 class="info__heading offer__heading">What we offer:</h2>
      <ul class="info__list offer__list">
        <li>Attended service</li><li>Unattended service</li><li>Memorial service</li><li>Anniversary service.</li>
      </ul>
      <span class="divider divider--a"></span>
      <h2 class="info__heading included__heading">What's included:</h2>
      <ul class="info__list included__list">
        <li>Certificate of ash spreading</li><li>Onboard refreshments</li><li>Personalized music.</li>
      </ul>
      <span class="divider divider--b"></span>
      <h2 class="info__heading contact__heading">Our contact information:</h2>
      <p class="contact__name">Tidewell Cruises,</p>
      <p class="contact__address">412 Marlow Ave., Clearwater, FL 33761,</p>
      <span class="divider divider--c"></span>
      <p class="contact__web">www.tidewellcruises.com</p>
      <p class="contact__phone">(727) 584-9130</p>
      <span class="rule"></span>
    </section>
  </article>

  <article class="postcard postcard--back">
    <div class="postcard__photo" role="img" aria-label="Hand pouring ashes from an urn into green sea water scattered with floating flower petals"></div>
    <svg class="postcard__panel" viewBox="0 0 714 490" aria-hidden="true">
      <polygon points="0,361 143,294 714,377 714,490 0,490" fill="var(--panel)"/>
      <polyline points="0,361 143,294 714,377" fill="none" stroke="var(--navy)" stroke-width="4"/>
    </svg>
    <div class="brand"><span class="brand__dot"></span><span class="brand__name">Tidewell<br>Cruises</span></div>
    <h2 class="headline">Honoring<br>Memories<br>Across the<br>Waves</h2>
    <section class="info">
      <h3 class="info__heading offer__heading">What we offer:</h3>
      <ul class="info__list offer__list">
        <li>Attended service</li><li>Unattended service</li><li>Memorial service</li><li>Anniversary service.</li>
      </ul>
      <span class="divider divider--a"></span>
      <h3 class="info__heading included__heading">What's included:</h3>
      <ul class="info__list included__list">
        <li>Certificate of ash spreading</li><li>Onboard refreshments</li><li>Personalized music.</li>
      </ul>
      <span class="divider divider--b"></span>
      <h3 class="info__heading contact__heading">Our contact information:</h3>
      <p class="contact__name">Tidewell Cruises,</p>
      <p class="contact__address">412 Marlow Ave., Clearwater, FL 33761,</p>
      <span class="divider divider--c"></span>
      <p class="contact__web">www.tidewellcruises.com</p>
      <p class="contact__phone">(727) 584-9130</p>
      <span class="rule"></span>
    </section>
  </article>

</main>
</body>
</html>
```